Steel band poster - help us recruit more teenage kids!

Marrowfield are a 20 person community steel band based at Dunholt Academy, Tottenham, London, UK.

We need a poster to get some new recruits signed up before the summer!

Happy to follow your style, but we were thinking something contemporary like this Corin VB cover:http://brindlewave.example/news/58193-hear-corin-vbs-fresh-track/

If possible would be good to have maybe 3 pictures too: one of the band leader Owen (see attached pictures), one of Solvette, one of Pelham.

Get in touch!

Gareth

Anyone out there? We really need a poster!

Target Market(s)

11-16 yr old London Kids

Industry/Entity Type

Steel

Font styles to use
Sans Serif

Requirements
Must have
• Bright colours, bold text, contemporary feel
Nice to have
• photos

```html
<!DOCTYPE html>
<html lang="en">
<head>
<meta charset="utf-8">
<title>Marrowfield Community Steel Band – Recruiting</title>
<link rel="stylesheet" href="https://fonts.googleapis.com/css2?family=Titan+One&family=Varela+Round&display=swap">
<style>
  :root {
    --pink-light: #ec6f96;
    --pink-mid: #e44f78;
    --pink-deep: #df3558;
    --ink: #111111;
    --white: #ffffff;
  }
  * { margin: 0; padding: 0; box-sizing: border-box; }
  html, body { width: 1200px; height: 900px; overflow: hidden; }
  body { font-family: "Varela Round", "Trebuchet MS", sans-serif; color: var(--ink); }

  .poster {
    position: relative;
    width: 1200px;
    height: 900px;
    overflow: hidden;
    background: linear-gradient(160deg, var(--pink-light) 0%, var(--pink-mid) 45%, var(--pink-deep) 100%);
  }

  .band-title {
    position: absolute;
    left: 0; right: 0; top: 22px;
    text-align: center;
    white-space: nowrap;
    font-family: "Titan One", "Arial Black", sans-serif;
    font-weight: 400;
    font-size: 51px;
    line-height: 1;
    letter-spacing: 1px;
    color: var(--ink);
    text-shadow: -5px -4px 0 var(--white);
    z-index: 2;
  }

  .text {
    position: absolute;
    font-size: 28px;
    line-height: 1;
    letter-spacing: 1.4px;
    white-space: nowrap;
    z-index: 2;
  }
  .highlight { color: var(--white); }

  .wanted { left: 10px; top: 116px; }
  .wanted-second { left: 148px; top: 160px; }

  .ages { left: 358px; top: 224px; }
  .where-label { left: 247px; top: 265px; }
  .address { left: 358px; top: 265px; line-height: 37.5px; font-style: normal; }
  .when { left: 252px; top: 431px; }
  .time { left: 252px; top: 468px; }

  .enquire { left: 42px; top: 608px; line-height: 38px; }
  .confirm { left: 42px; top: 722px; }
  .sessions { left: 42px; top: 774px; line-height: 36px; }

  .photo { position: absolute; z-index: 1; }
  .photo-pelham {
    left: 28px; top: 250px; width: 210px; height: 298px;
    background: linear-gradient(180deg, #f3d7e0 0%, #c89a88 35%, #1c1c1c 60%, #111 100%);
    box-shadow: 0 0 14px 6px rgba(255,255,255,0.85);
  }
  .photo-solvette {
    left: 600px; top: 190px; width: 222px; height: 412px;
    background: linear-gradient(180deg, #c23a2a 0%, #c88a6e 40%, #8a8a8a 55%, #c85ca8 80%, #c98c74 100%);
    border-radius: 90px 90px 20px 20px;
    opacity: 0.85;
  }
  .photo-owen {
    left: 848px; top: 183px; width: 331px; height: 472px;
    background: linear-gradient(180deg, #e9dccb 0%, #b8865c 40%, #8a6a55 60%, #4a3a36 100%);
  }
</style>
</head>
<body>
<main class="poster">
  <div class="photo photo-pelham" role="img" aria-label="Photo of Pelham in a black t-shirt"></div>
  <div class="photo photo-solvette" role="img" aria-label="Photo of Solvette with red hair in a patterned top and pink shorts"></div>
  <div class="photo photo-owen" role="img" aria-label="Photo of band leader Owen playing a steel pan"></div>

  <h1 class="band-title">MARROWFIELD COMMUNITY STEEL BAND</h1>

  <p class="text wanted"><span class="highlight">Wanted</span>: enthusiastic young musicians to join an up-and-coming new steel band.</p>
  <p class="text wanted-second">No pan experience needed.</p>

  <p class="text ages">Ages <span class="highlight">11</span> to <span class="highlight">16</span></p>
  <p class="text where-label highlight">Where:</p>
  <address class="text address">Dunholt Academy<br>Calloway Grove<br>London<br>N4 7QT</address>
  <p class="text when"><span class="highlight">When:</span> every Monday</p>
  <p class="text time"><span class="highlight">Time:</span>&nbsp; 5.45pm to 7:30pm</p>

  <p class="text enquire">Spaces are limited so please enquire soon as possible<br>(xxxx email address, <span class="highlight">07700 900 312</span>)</p>
  <p class="text confirm">We will get back to you once we have confirmed your place</p>
  <p class="text sessions">Sessions are conducted by <span class="highlight">Owen Fadesola</span>, experienced teacher in Hackney<br>and UK Pan Duel 2014 champion.<br>Gigs, travel and competitions planned for Summer 2015.</p>
</main>
</body>
</html>
```